Business Card Design

We like to use greens as you will see in our logo (but not TOO much green). We are a Dental Clinic in a somewhat eccentric community. We do not like the dated sharp designs which we see many dentists use. We're looking for something bright and fresh while still maintaining the integrity of the profession. Elegance is not necessarily what we are going for... we need for the design to be "mature" but also up-lifting.

See our logo.
Updates

Project Deadline Extended
Reason: We have 5 designs which we like. But we'd like to see a few more before committing to a design.

Project Deadline Extended
Reason: We are awaiting revisions to this project. We are still welcoming designs while we wait to see if designers are able to provide to us the revisions we require in order to proceed with a selection.

Target Market(s)

Younger families - ages late 20's to early 40's

Industry/Entity Type

Business

Contact Information for Business Card

Marlow T. Venn DDS 2737 S. Fennimore Ave. Ste. 8 Royal Oak, MI 48059 (248)555-0174 FX (248)555-0189 info@BrightwaveDentalMi.example BrigthwaveDentalMi.example on the back of the card we need an appointment reminder (For____ Date___ Time____) with "If you are unable to keep your appointment, kindly give 48 hours notice" at the bottom. No use of teeth in the design. DOUBLE SIDED DESIGN

Requirements
Should not have
• The use of pictures of teeth

```html
<!DOCTYPE html>
<html lang="en">
<head>
<meta charset="utf-8">
<title>Brightwave Dental Care – Business Card</title>
<link rel="stylesheet" href="https://fonts.googleapis.com/css2?family=PT+Sans:ital,wght@0,400;0,700;1,400&family=Cinzel:wght@500&display=swap">
<style>
  :root {
    --forest: #1e6b34;
    --leaf: #7ccc2a;
    --paper: #ffffff;
    --ink: #3a3a3a;
    --rule: #6d6d6d;
    --backdrop: #ecebe6;
    --edge: #5a5a5a;
  }
  * { margin: 0; padding: 0; box-sizing: border-box; }
  html, body { width: 1200px; height: 1178px; overflow: hidden; }
  body {
    position: relative;
    background: var(--backdrop);
    font-family: "PT Sans", Arial, sans-serif;
    color: var(--ink);
  }
  .card {
    position: absolute;
    width: 916px;
    height: 523px;
    border-radius: 32px;
    background: var(--paper);
    overflow: hidden;
    border: 1.5px solid var(--edge);
  }
  .card--front { left: 38px; top: 47px; }
  .card--back { left: 236px; top: 620px; }

  .front-waves { position: absolute; inset: 0; width: 916px; height: 523px; }

  .brand { position: absolute; color: var(--forest); font-weight: 700; line-height: 1; }
  .brand__name { display: block; }
  .brand__tag { display: block; text-transform: uppercase; letter-spacing: 2px; }
  .card--front .brand { left: 74px; top: 78px; }
  .card--front .brand__name { font-size: 82px; }
  .card--front .brand__tag { font-size: 42px; margin-top: 10px; }
  .card--back .brand { left: 71px; top: 40px; }
  .card--back .brand__name { font-size: 52px; }
  .card--back .brand__tag { font-size: 26px; margin-top: 6px; }

  .dentist {
    position: absolute; left: 76px; top: 320px;
    font-size: 29px; font-weight: 700; color: var(--forest);
  }
  .dentist__title { font-weight: 400; color: var(--ink); font-size: 25px; }

  .contact {
    position: absolute; right: 25px; top: 286px;
    list-style: none; text-align: right; color: var(--paper); font-size: 22px;
  }
  .contact li { height: 39.5px; display: flex; justify-content: flex-end; align-items: center; gap: 6px; }
  .contact svg { width: 18px; height: 18px; fill: var(--paper); }
  .address {
    position: absolute; right: 25px; top: 466px;
    color: var(--paper); font-size: 22px;
  }

  .appointment__title {
    position: absolute; left: 77px; top: 160px;
    font-family: "Cinzel", Georgia, serif; font-size: 31px; color: var(--forest);
  }
  .field { position: absolute; font-size: 25px; color: var(--ink); line-height: 1; }
  .dots { position: absolute; height: 0; border-bottom: 2px dotted var(--rule); }
  .slot { position: absolute; border: 2px solid var(--edge); border-radius: 4px; height: 35px; }

  .days { position: absolute; right: 24px; top: 76px; list-style: none; }
  .days li {
    position: absolute; right: 0; display: flex; align-items: center; gap: 14px;
    font-size: 25px; font-weight: 700; color: var(--ink);
  }
  .days .slot { position: static; width: 57px; height: 33px; }

  .notice {
    position: absolute; left: 0; right: 0; top: 454px; text-align: center;
    font-style: italic; font-size: 23.5px; color: var(--ink); padding-left: 48px;
  }
</style>
</head>
<body>

<section class="card card--front">
  <svg class="front-waves" viewBox="0 0 916 523" aria-hidden="true">
    <path fill="var(--forest)" d="M0,472 C270,478 590,330 850,0 L916,0 L916,523 L0,523 Z"/>
    <path fill="var(--leaf)" d="M0,378 C160,445 420,405 662,282 C430,425 210,472 0,446 Z"/>
  </svg>

  <div class="brand">
    <span class="brand__name">Brightwave</span>
    <span class="brand__tag">Dental Care</span>
  </div>

  <p class="dentist">Marlow T. Venn, <span class="dentist__title">DDS</span></p>

  <ul class="contact">
    <li>
      <svg viewBox="0 0 24 24"><path d="M6.6 10.8a15 15 0 0 0 6.6 6.6l2.2-2.2a1 1 0 0 1 1-.25 11.4 11.4 0 0 0 3.6.6 1 1 0 0 1 1 1V20a1 1 0 0 1-1 1A17 17 0 0 1 3 4a1 1 0 0 1 1-1h3.5a1 1 0 0 1 1 1c0 1.25.2 2.45.6 3.6a1 1 0 0 1-.25 1Z"/></svg>
      (248)555-0174
    </li>
    <li>
      <svg viewBox="0 0 24 24"><path d="M6 3h9l3 3v4H6Zm-2 8h16a2 2 0 0 1 2 2v5h-4v3H6v-3H2v-5a2 2 0 0 1 2-2Zm4 5v3h8v-3Z"/></svg>
      (248)555-0189
    </li>
    <li>
      <svg viewBox="0 0 24 24"><path d="M12 2a10 10 0 1 0 0 20 10 10 0 0 0 0-20Zm6.9 9h-3a15 15 0 0 0-1.3-6.1A8 8 0 0 1 18.9 11ZM12 4c.9 1.2 1.8 3.6 1.9 7h-3.8C10.2 7.6 11.1 5.2 12 4ZM9.4 4.9A15 15 0 0 0 8.1 11h-3a8 8 0 0 1 4.3-6.1ZM5.1 13h3a15 15 0 0 0 1.3 6.1A8 8 0 0 1 5.1 13ZM12 20c-.9-1.2-1.8-3.6-1.9-7h3.8c-.1 3.4-1 5.8-1.9 7Zm2.6-.9a15 15 0 0 0 1.3-6.1h3a8 8 0 0 1-4.3 6.1Z"/></svg>
      BrigthwaveDentalMi.example
    </li>
    <li>
      <svg viewBox="0 0 24 24"><path d="M2 6a2 2 0 0 1 2-2h16a2 2 0 0 1 2 2v12a2 2 0 0 1-2 2H4a2 2 0 0 1-2-2Zm2 .5V8l8 5 8-5V6.5l-8 5Z"/></svg>
      info@BrightwaveDentalMi.example
    </li>
  </ul>

  <p class="address">2737 S. Fennimore Ave. Ste. 8 Royal Oak, MI 48059</p>
</section>

<section class="card card--back">
  <div class="brand">
    <span class="brand__name">Brightwave</span>
    <span class="brand__tag">Dental Care</span>
  </div>

  <h2 class="appointment__title">YOUR APPOINTMENT</h2>

  <span class="field" style="left:79px; top:250px;">Name :</span>
  <span class="dots" style="left:181px; width:502px; top:272px;"></span>

  <span class="field" style="left:79px; top:315px;">Date :</span>
  <span class="dots" style="left:184px; width:163px; top:337px;"></span>
  <span class="field" style="left:357px; top:315px;">Time :</span>
  <span class="dots" style="left:438px; width:157px; top:337px;"></span>
  <span class="field" style="left:599px; top:315px;">am / pm</span>

  <span class="field" style="left:79px; top:380px;">Next Appointment</span>
  <span class="slot" style="left:326px; top:374px; width:164px;"></span>
  <span class="slot" style="left:528px; top:374px; width:165px;"></span>

  <ul class="days">
    <li style="top:0;">MON <span class="slot"></span></li>
    <li style="top:63px;">TUE <span class="slot"></span></li>
    <li style="top:126px;">WED <span class="slot"></span></li>
    <li style="top:193px;">THU <span class="slot"></span></li>
    <li style="top:246px;">FRI <span class="slot"></span></li>
    <li style="top:303px;">SAT <span class="slot"></span></li>
  </ul>

  <p class="notice">If you are unable to keep your appointment, kindly give 48 hours notice</p>
</section>

</body>
</html>
```